Business Cards for a small business advisory (business services)

Professional look. Same as would apply for a lawyer, accountant, or other financial services professional. Please use the logo colors

Target Market(s)

small business owners

Industry/Entity Type

Financial Servics

Contact Information for Business Card

Name: Gavin L. Whitmore, CAIA / Title: Business Advisor / Office #: (718) 294-7716 / Mobile #: (917) 382-5047 / Email: g.whitmore@clearfieldventurepartners.example / Web: www.clearfieldventurepartners.example

Font styles to use
Sans Serif

```html
<!DOCTYPE html>
<html lang="en">
<head>
<meta charset="utf-8">
<title>Clearfield Venture Partners – Business Cards</title>
<link href="https://fonts.googleapis.com/css2?family=Montserrat:wght@600;700&family=Quicksand:wght@400;500&display=swap" rel="stylesheet">
<style>
  :root {
    --navy: #324a7a;
    --green: #8dc64b;
    --white: #ffffff;
    --backdrop: #e4e6e9;
  }
  * { margin: 0; padding: 0; box-sizing: border-box; }
  html, body {
    width: 1200px;
    height: 780px;
    overflow: hidden;
    background: var(--backdrop);
  }
  .sheet {
    position: relative;
    width: 1200px;
    height: 780px;
  }
  .card {
    position: absolute;
    left: 290px;
    width: 620px;
    height: 354px;
    overflow: hidden;
    background: var(--white);
    box-shadow: 0 6px 18px rgba(0, 0, 0, 0.18);
  }
  .card--front { top: 21px; }
  .card--back { top: 405px; }
  .card__art {
    position: absolute;
    inset: 0;
    width: 620px;
    height: 354px;
  }
  .brand {
    position: absolute;
    left: 78px;
    top: 118px;
    width: 320px;
    display: flex;
    align-items: center;
    gap: 14px;
  }
  .brand__dot {
    width: 24px;
    height: 24px;
    flex: none;
    border-radius: 50%;
    background: var(--navy);
  }
  .brand__name {
    font-family: "Montserrat", sans-serif;
    font-weight: 700;
    font-size: 30px;
    line-height: 34px;
    color: var(--navy);
    letter-spacing: -0.3px;
  }
  .brand__line { display: block; white-space: nowrap; }
  .web-line {
    position: absolute;
    left: 122px;
    top: 314px;
    display: flex;
    align-items: center;
    gap: 12px;
    font-family: "Quicksand", sans-serif;
    font-weight: 500;
    font-size: 19px;
    color: var(--white);
    white-space: nowrap;
  }
  .icon { width: 20px; height: 20px; flex: none; }
  .person {
    position: absolute;
    left: 40px;
    top: 110px;
  }
  .person__name {
    font-family: "Montserrat", sans-serif;
    font-weight: 600;
    font-size: 27px;
    color: var(--navy);
    white-space: nowrap;
  }
  .person__title {
    margin-top: 4px;
    font-family: "Montserrat", sans-serif;
    font-weight: 600;
    font-size: 15px;
    letter-spacing: 9px;
    color: var(--green);
  }
  .contacts {
    position: absolute;
    left: 58px;
    top: 222px;
    list-style: none;
    font-family: "Quicksand", sans-serif;
    font-weight: 500;
    font-size: 18px;
    line-height: 29px;
    color: var(--white);
    white-space: nowrap;
  }
  .contacts li {
    display: flex;
    align-items: center;
    gap: 12px;
  }
  .contacts .icon { width: 17px; height: 17px; }
</style>
</head>
<body>
<main class="sheet">

  <section class="card card--front" aria-label="Card front">
    <svg class="card__art" viewBox="0 0 620 354" aria-hidden="true">
      <rect width="620" height="354" fill="var(--white)"/>
      <rect width="620" height="18" fill="var(--navy)"/>
      <path d="M0 300 H370 C440 300 480 272 540 264 C580 258 605 258 620 258 V354 H0 Z" fill="var(--navy)"/>
      <circle cx="590" cy="95" r="166" fill="var(--white)"/>
      <circle cx="590" cy="95" r="150" fill="var(--green)"/>
      <circle cx="615" cy="82" r="124" fill="var(--navy)"/>
      <path d="M0 108 H28 Q42 108 42 122 V232 Q42 246 28 246 H0 Z" fill="var(--navy)"/>
    </svg>

    <div class="brand">
      <span class="brand__dot"></span>
      <span class="brand__name">
        <span class="brand__line">Clearfield</span>
        <span class="brand__line">Venture Partners</span>
      </span>
    </div>

    <div class="web-line">
      <svg class="icon" viewBox="0 0 20 20" aria-hidden="true" fill="none" stroke="var(--white)" stroke-width="1.6">
        <circle cx="10" cy="10" r="8"/>
        <ellipse cx="10" cy="10" rx="3.5" ry="8"/>
        <line x1="2" y1="10" x2="18" y2="10"/>
      </svg>
      <span>www.clearfieldventurepartners.example</span>
    </div>
  </section>

  <section class="card card--back" aria-label="Card back">
    <svg class="card__art" viewBox="0 0 620 354" aria-hidden="true">
      <rect width="620" height="354" fill="var(--white)"/>
      <rect width="620" height="14" fill="var(--navy)"/>
      <path d="M0 205 H430 C470 205 495 250 540 262 C580 272 605 264 620 256 V354 H0 Z" fill="var(--navy)"/>
      <circle cx="580" cy="110" r="156" fill="var(--white)"/>
      <circle cx="580" cy="110" r="140" fill="var(--green)"/>
      <circle cx="598" cy="98" r="116" fill="var(--navy)"/>
    </svg>

    <div class="person">
      <h1 class="person__name">Gavin L. Whitmore, CAIA</h1>
      <p class="person__title">Advisor</p>
    </div>

    <ul class="contacts">
      <li>
        <svg class="icon" viewBox="0 0 20 20" aria-hidden="true">
          <path d="M4 2 L7.5 2 L9 6.5 L6.8 8 C7.8 10.3 9.7 12.2 12 13.2 L13.5 11 L18 12.5 L18 16 C18 17.1 17.1 18 16 18 C8.3 18 2 11.7 2 4 C2 2.9 2.9 2 4 2 Z" fill="var(--white)"/>
        </svg>
        <span>(718) 294-7716</span>
      </li>
      <li>
        <svg class="icon" viewBox="0 0 20 20" aria-hidden="true">
          <rect x="5" y="1" width="10" height="18" rx="2" fill="var(--white)"/>
          <rect x="7" y="4" width="6" height="9" fill="var(--navy)"/>
          <circle cx="10" cy="16" r="1.2" fill="var(--navy)"/>
        </svg>
        <span>(917) 382-5047</span>
      </li>
      <li>
        <svg class="icon" viewBox="0 0 20 20" aria-hidden="true">
          <rect x="1" y="4" width="18" height="12" fill="var(--white)"/>
          <path d="M1.5 4.5 L10 11 L18.5 4.5" fill="none" stroke="var(--navy)" stroke-width="1.4"/>
        </svg>
        <span>g.whitmore@clearfieldventurepartners.example</span>
      </li>
      <li>
        <svg class="icon" viewBox="0 0 20 20" aria-hidden="true" fill="none" stroke="var(--white)" stroke-width="1.6">
          <circle cx="10" cy="10" r="8"/>
          <ellipse cx="10" cy="10" rx="3.5" ry="8"/>
          <line x1="2" y1="10" x2="18" y2="10"/>
        </svg>
        <span>www.clearfieldventurepartners.example</span>
      </li>
    </ul>
  </section>

</main>
</body>
</html>
```